Zielgruppe
wir sind ein ambulanter Pflegedienst
Aufgabenstellung
Es soll ein Flyer entworfen werden.
Im Vordergrund steht die Behandlungspflege. Patienten sollen darauf aufmerksam gemacht werden, dass wir Insulininjektionen übernehmen und Kompressionsstrümpfe anziehen, wenn der Hausarzt dafür eine Verordnung ausstellt.
Im Vordergrund steht die Insulininjektion und das an und ausziehen der Kompressionsstrümpfe.
Falls die Patienten es nicht mehr alleine schaffen, springt der Pflegedienst ein.
Wichtig ist, dass das Pflegegeld nicht gekürzt wird, da dies eine Leistung der Krankenkasse ist.
Daten des Pflegedienstes:
Pflegehaus Lindental
Birkenweg 27
18057 Rostock
Tel 0800 4417236
www.Pflegehaus-Lindental.de
info@Pflegehaus-Lindental.de

```html
<!DOCTYPE html>
<html lang="de">
<head>
<meta charset="utf-8">
<title>Behandlungspflege – Pflegehaus Lindental</title>
<link rel="stylesheet" href="https://fonts.googleapis.com/css2?family=Roboto:wght@500;700&display=swap">
<style>
  :root {
    --green: #67ad34;
    --orange: #f08a2c;
    --text: #55585b;
    --logo-blue: #1f5fa8;
    --stage: #d9d9d9;
    --white: #ffffff;
  }
  html, body {
    margin: 0;
    width: 1200px;
    height: 675px;
    overflow: hidden;
    background: var(--stage);
    font-family: "Roboto", Arial, sans-serif;
  }
  .flyer {
    position: absolute;
    left: 144px;
    top: 15px;
    width: 1470px;
    height: 1038px;
    transform: scale(0.62);
    transform-origin: 0 0;
    background: var(--white);
    overflow: hidden;
  }
  .backdrop {
    position: absolute;
    inset: 0;
    background: linear-gradient(135deg, #fbfbfa 0%, #f1efec 45%, #e9ebea 75%, #f6f6f5 100%);
  }
  .title-band {
    position: absolute;
    left: 560px; top: 0;
    width: 670px; height: 189px;
    background: var(--green);
  }
  .title {
    position: absolute;
    left: 600px; top: 62px;
    width: 600px;
    margin: 0;
    text-align: center;
    color: var(--white);
    font-size: 60px;
    font-weight: 700;
    letter-spacing: 0.5px;
  }
  .brand {
    position: absolute;
    left: 1280px; top: 30px;
    width: 170px; height: 165px;
    display: flex; flex-direction: column; align-items: center; justify-content: center;
    gap: 10px;
    text-align: center;
  }
  .brand-dot {
    width: 84px; height: 84px;
    border-radius: 50%;
    background: var(--green);
  }
  .brand-name {
    color: var(--green);
    font-weight: 700;
    font-size: 20px;
    line-height: 1.1;
  }
  .photo-layer { position: absolute; inset: 0; }
  .call-band {
    position: absolute;
    left: 0; top: 959px;
    width: 1470px; height: 79px;
    background: var(--orange);
  }
  .call-line {
    position: absolute;
    left: 672px; top: 959px;
    height: 79px;
    display: flex; align-items: center; gap: 16px;
    color: var(--white);
    font-weight: 700;
    font-size: 46px;
  }
  .content {
    position: absolute;
    left: 735px; top: 205px;
    width: 700px;
    color: var(--text);
    font-size: 22px;
    font-weight: 500;
    line-height: 25px;
  }
  .content p { margin: 0 0 24px; }
  .section-head {
    margin: 0 0 32px;
    color: var(--green);
    font-size: 50px;
    font-weight: 700;
    line-height: 60px;
    text-decoration: underline;
    text-decoration-thickness: 3px;
    text-underline-offset: 6px;
  }
  .highlights {
    list-style: none;
    margin: 0 0 20px;
    padding: 0 0 0 62px;
    color: var(--orange);
    font-size: 26px;
    font-weight: 700;
  }
  .highlights li { margin-bottom: 22px; }
  .highlights li::before { content: "•"; margin-right: 4px; }
  .contact p { margin: 0 0 24px; }
</style>
</head>
<body>
  <div class="flyer">
    <div class="backdrop" role="img" aria-label="Blasser Hintergrund mit Stethoskop, Spritze und Verbandsmaterial"></div>

    <div class="title-band"></div>
    <h1 class="title">Behandlungspflege</h1>

    <div class="brand">
      <div class="brand-dot"></div>
      <div class="brand-name">Pflegehaus<br>Lindental</div>
    </div>

    <div class="call-band"></div>

    <svg class="photo-layer" width="1470" height="1038" viewBox="0 0 1470 1038">
      <defs>
        <linearGradient id="skin" x1="0" y1="0" x2="1" y2="1">
          <stop offset="0" stop-color="#e9e4df"/>
          <stop offset="0.35" stop-color="#c9957a"/>
          <stop offset="1" stop-color="#9b6a52"/>
        </linearGradient>
        <linearGradient id="stocking" x1="0" y1="0" x2="1" y2="1">
          <stop offset="0" stop-color="#fbf8f4"/>
          <stop offset="1" stop-color="#f1e6da"/>
        </linearGradient>
      </defs>
      <circle cx="100" cy="530" r="595" fill="url(#skin)" stroke="var(--orange)" stroke-width="9"
              role="img" aria-label="Foto: Insulininjektion mit einer Spritze in die Bauchhaut"/>
      <circle cx="180" cy="906" r="180" fill="url(#stocking)" stroke="var(--orange)" stroke-width="6"
              role="img" aria-label="Foto: hautfarbener Kompressionsstrumpf"/>
      <rect x="30" y="800" width="270" height="210" rx="40" fill="#d9a56f" opacity="0.85"/>
    </svg>

    <div class="call-line">
      <svg width="54" height="54" viewBox="0 0 54 54" aria-hidden="true">
        <circle cx="27" cy="27" r="24" fill="none" stroke="#1a1a1a" stroke-width="3"/>
        <path d="M19 14c2-1 4 0 5 2l2 5c1 2 0 3-1 4l-2 1c1 4 4 7 8 9l1-2c1-1 2-2 4-1l5 2c2 1 3 3 2 5l-1 2c-1 2-3 3-6 2-9-3-16-10-19-19-1-3 0-6 2-7z" fill="#1a1a1a"/>
      </svg>
      <span>0800 44172 36 (kostenfrei)</span>
    </div>

    <section class="content">
      <h2 class="section-head">Unsere Leistungen:</h2>
      <p>Mit unserem Fachpersonal sind wir vom ambulanten Pflegehaus Lindental Ihre Experten für ärztlich verordnete Behandlungen.</p>
      <p>Als auf Diabetes Patienten spezialisierter Pflegedienst übernehmen wir auch</p>
      <ul class="highlights">
        <li>Insulininjektionen und Blutzuckerkontrollen</li>
        <li>Kompressionsstrümpfe an- und ausziehen</li>
      </ul>
      <p>und weitere med. Behandlungspflegen nach neuesten, fachlichen Erkenntnissen.</p>
      <p>Das Pflegegeld wird nicht gekürzt, da dies eine Leistung der Krankenkasse ist.</p>
      <div class="contact">
        <p>Informieren Sie sich unter:</p>
        <p>Pflegehaus Lindental<br>Birkenweg 27<br>18057 Rostock<br>Tel.:&nbsp; 0800 4417236 (kostenfrei)</p>
        <p>www.Pflegehaus-Lindental.de<br>info@Pflegehaus-Lindental.de</p>
      </div>
    </section>
  </div>
</body>
</html>
```